TriVex Business Card Design - double sided -plumbing local plumbing company

We have a Plumbing company where the design was create through Sketch Hive. We would now like a business card designed as well. We want it to be in the colour version of the logo.

Details below for the card.

Phone Number: 0438 615 247
Email: info@trivexplumbing.example.au
Website: https://trivexplumbing.example.au
We really want a sophisticated design that stand out from the other- informative and timeless.

Target Market(s)

local Canberra market

Industry/Entity Type

Plumbing, gas fitting, hot water

Contact Information for Business Card

Phone number, email, logo and "Supplying all your heating, cooling and hot water needs"

Requirements
Must have
• bust be colourful, must also be though about it being printed on a magnet. must Vex with the logo - I dont want the logo and information chucked onto a white canvas I would prefer it to be smooth and look purposeful

```html
<!DOCTYPE html>
<html lang="en">
<head>
<meta charset="utf-8">
<title>TriVex Plumbing – Business Card</title>
<link rel="stylesheet" href="https://fonts.googleapis.com/css2?family=Roboto:wght@400;500;700;900&display=swap">
<style>
  :root {
    --backdrop: #2b2b2d;
    --card: #141416;
    --card-edge: #1d1d20;
    --emboss: #5a5a61;
    --blue: #1b8fd8;
    --orange: #f5ab2b;
    --white: #f2f2f2;
    --ink: #1a1a1a;
  }
  * { margin: 0; padding: 0; box-sizing: border-box; }
  html, body {
    width: 1200px; height: 852px; overflow: hidden;
    background: var(--backdrop);
    font-family: "Roboto", Arial, sans-serif;
  }
  .stage { position: relative; width: 1200px; height: 852px; }
  .card {
    position: absolute; left: 340px; width: 520px; height: 300px;
    background: var(--card); border-radius: 18px; overflow: hidden;
    box-shadow: 0 14px 30px rgba(0,0,0,.45);
    border: 1px solid var(--card-edge);
  }
  .card--front { top: 90px; }
  .card--back { top: 462px; }

  /* Front */
  .front-brand {
    position: absolute; left: 0; right: 0; top: 98px; text-align: center;
    font-weight: 900; color: var(--emboss); line-height: 1;
    text-shadow: 0 1px 0 rgba(255,255,255,.08), 0 -1px 0 rgba(0,0,0,.6);
  }
  .front-brand .name { font-size: 62px; letter-spacing: 2px; display: block; }
  .front-brand .trade { font-size: 22px; letter-spacing: 10px; display: block; margin-top: 4px; }
  .tagline {
    position: absolute; left: 0; right: 0; top: 210px; text-align: center;
    font-size: 14px; color: var(--white); letter-spacing: .2px;
  }
  .tagline .warm { color: var(--orange); }
  .tagline .cool { color: var(--blue); }

  /* Back */
  .back-mark {
    position: absolute; right: -70px; top: -30px; width: 300px; height: 300px;
  }
  .back-brand {
    position: absolute; left: 34px; top: 56px; color: var(--blue);
    font-weight: 900; line-height: 1;
  }
  .back-brand .name { font-size: 44px; letter-spacing: 1px; display: block; }
  .back-brand .trade { font-size: 17px; letter-spacing: 7px; display: block; margin-top: 4px; }
  .accent-line {
    position: absolute; right: 0; bottom: 60px; width: 190px; height: 6px;
    background: var(--orange);
  }
  .contact { position: absolute; left: 34px; top: 166px; color: var(--white); }
  .contact .phone {
    display: flex; align-items: center; gap: 8px;
    font-size: 22px; font-weight: 700; color: var(--blue); letter-spacing: 1.5px;
  }
  .contact .phone svg { width: 16px; height: 16px; }
  .contact .line { font-size: 14px; margin-top: 5px; padding-left: 24px; }
  .tag-band {
    position: absolute; left: 0; right: 0; bottom: 0; height: 38px;
    background: var(--orange); color: var(--ink);
    font-size: 14px; font-weight: 500; line-height: 38px; padding-left: 34px;
  }
</style>
</head>
<body>
<main class="stage">
  <section class="card card--front" aria-label="Card front">
    <div class="front-brand">
      <span class="name">TriVex</span>
      <span class="trade">PLUMBING</span>
    </div>
    <p class="tagline">Supplying all your <span class="warm">heating</span>, <span class="cool">cooling</span> and <span class="warm">hot water</span> needs</p>
  </section>

  <section class="card card--back" aria-label="Card back">
    <svg class="back-mark" viewBox="0 0 300 300" aria-hidden="true">
      <defs>
        <radialGradient id="ringGlow" cx="40%" cy="35%" r="70%">
          <stop offset="0" stop-color="#3a3a3f"/>
          <stop offset="1" stop-color="#18181b"/>
        </radialGradient>
      </defs>
      <circle cx="150" cy="150" r="135" fill="url(#ringGlow)"/>
    </svg>
    <div class="back-brand">
      <span class="name">TriVex</span>
      <span class="trade">PLUMBING</span>
    </div>
    <div class="accent-line"></div>
    <div class="contact">
      <div class="phone">
        <svg viewBox="0 0 16 16" aria-hidden="true">
          <circle cx="8" cy="8" r="7.5" fill="var(--orange)"/>
          <path d="M5.2 4.2l1.4-.3.8 1.9-.9.7c.4.9 1.1 1.6 2 2l.7-.9 1.9.8-.3 1.4c-3.1.2-5.8-2.5-5.6-5.6z" fill="var(--ink)"/>
        </svg>
        0438 615 247
      </div>
      <p class="line">info@trivexplumbing.example.au</p>
      <p class="line">https://trivexplumbing.example.au</p>
    </div>
    <div class="tag-band">Supplying all your heating, cooling and hot water needs</div>
  </section>
</main>
</body>
</html>
```